Anwaltskanzlei sucht Design für Geschäftspapier, Visitenkarten, Marketing unter Einbindung des neuen Logos
Zielgruppe
Anwaltliche Rechtsberatung und Rechtsvertretung auf den Gebieten des Arbeits-, Gesellschafts- und Wirtschaftsrechts sowie des Datenschutzrechts
Zielgruppe: Mittelständische Unternehmen aller Rechtsformen und Branchen
In Kooperation mit Kanzlei Velbrand (www.kanzlei-velbrand.de)
Inhaber einer weiteren Kanzlei Velbrand & Krüger
Aufgabenstellung
Einbindung des übersandten Logos
ggf. Slogan: Kanzlei für den Mittelstand
optional: Nennung der Rechtsgebiete

```html
<!DOCTYPE html>
<html lang="de">
<head>
<meta charset="utf-8">
<title>Anwaltskanzlei Hossmer – Visitenkarte</title>
<link href="https://fonts.googleapis.com/css2?family=Montserrat:wght@400;500;600&display=swap" rel="stylesheet">
<style>
  :root {
    --navy: #212c4d;
    --stone: #b7b6bb;
    --paper: #ffffff;
    --stage: #e4e4e7;
    --slogan: #8d8d97;
    --mark-grey: #b8b7bc;
  }
  * { margin: 0; padding: 0; box-sizing: border-box; }
  html, body {
    width: 1200px; height: 720px; overflow: hidden;
    background: var(--stage);
    font-family: "Montserrat", sans-serif;
  }
  .stage { position: relative; width: 1200px; height: 720px; }
  .card {
    position: absolute; top: 178px;
    width: 510px; height: 331px; overflow: hidden;
  }
  .card--front { left: 85px; background: var(--stone); }
  .card--back { left: 637px; background: var(--navy); }

  .front-shapes { position: absolute; inset: 0; }

  .brand {
    position: absolute; left: 26px; top: 30px;
    display: flex; align-items: center; gap: 8px;
    color: var(--navy);
  }
  .brand__square { width: 14px; height: 14px; background: var(--navy); }
  .brand__name {
    font-size: 10.5px; font-weight: 400; line-height: 1.15;
    letter-spacing: 0.04em; text-transform: uppercase;
  }

  .person {
    position: absolute; left: 283px; top: 66px; width: 200px;
    text-align: center;
  }
  .person__name { font-size: 22px; font-weight: 600; color: var(--navy); }
  .person__role { font-size: 16px; font-weight: 400; color: var(--paper); margin-top: 6px; }

  .contact { position: absolute; color: var(--navy); font-size: 13.5px; font-weight: 400; line-height: 1.2; }
  .contact__icon { position: absolute; fill: var(--navy); }
  .contact--phone { left: 283px; top: 187px; }
  .contact--mail { left: 303px; top: 215px; }
  .contact--address { left: 320px; top: 243px; }
  .icon--phone { left: 255px; top: 186px; }
  .icon--mail { left: 274px; top: 218px; }
  .icon--pin { left: 298px; top: 251px; }

  .back-name {
    position: absolute; left: 0; right: 0; top: 110px;
    text-align: center; color: var(--mark-grey);
    font-size: 40px; font-weight: 500; letter-spacing: 0.12em; text-transform: uppercase;
  }
  .slogan {
    position: absolute; left: 0; right: 0; top: 238px;
    text-align: center; color: var(--slogan);
    font-size: 17px; font-weight: 500;
  }
</style>
</head>
<body>
<div class="stage">
  <section class="card card--front">
    <svg class="front-shapes" width="510" height="331" viewBox="0 0 510 331" aria-hidden="true">
      <polygon points="0,0 283,0 79,331 0,331" fill="var(--paper)"/>
      <polygon points="192,0 258,0 54,331 -12,331" fill="var(--navy)"/>
    </svg>

    <div class="brand">
      <span class="brand__square"></span>
      <span class="brand__name">Anwaltskanzlei<br>Hossmer</span>
    </div>

    <div class="person">
      <p class="person__name">Name Surname</p>
      <p class="person__role">Lawyer</p>
    </div>

    <svg class="contact__icon icon--phone" width="16" height="16" viewBox="0 0 24 24" aria-hidden="true">
      <path d="M6.6 10.8a15.1 15.1 0 0 0 6.6 6.6l2.2-2.2c.3-.3.7-.4 1-.2 1.1.4 2.3.6 3.6.6.6 0 1 .4 1 1V20c0 .6-.4 1-1 1A17 17 0 0 1 3 4c0-.6.4-1 1-1h3.5c.6 0 1 .4 1 1 0 1.3.2 2.5.6 3.6.1.3 0 .7-.2 1z"/>
    </svg>
    <p class="contact contact--phone">+49 (0) 12345678910</p>

    <svg class="contact__icon icon--mail" width="17" height="12" viewBox="0 0 17 12" aria-hidden="true">
      <rect width="17" height="12" rx="1.5"/>
      <path d="M2 2.5l6.5 4.5 6.5-4.5M2 10l4.5-3.5M15 10l-4.5-3.5" stroke="#fff" stroke-width="1" fill="none"/>
    </svg>
    <p class="contact contact--mail">N.Surname@firm.de</p>

    <svg class="contact__icon icon--pin" width="13" height="17" viewBox="0 0 13 17" aria-hidden="true">
      <path d="M6.5 0A6.5 6.5 0 0 0 0 6.5C0 11 6.5 17 6.5 17S13 11 13 6.5A6.5 6.5 0 0 0 6.5 0z"/>
      <circle cx="6.5" cy="6.3" r="2" fill="none" stroke="#fff" stroke-width="1"/>
    </svg>
    <p class="contact contact--address">123 Av. ABCD City<br>Germany</p>
  </section>

  <section class="card card--back">
    <p class="back-name">Hossmer</p>
    <p class="slogan">Kanzlei für den Mittelstand</p>
  </section>
</div>
</body>
</html>
```